Header/Banner Design for Website

Looking for a banner/header design for www.fixerupperdiaries.net Should be fun and whimsical, and include the name of the website, something to do with Fixer Upper Diaries or tools, and a caricature of a young, beautiful 20 something blond who the website revolves around. The website is about a young woman who bought her first house and it taking on all of the renovations and remodeling on her own for the first time.

The header/banner should include the same colors that are in the website. The width should be no more than 430 pixels, the height is flexible but the current space in the header is 85 pixels...looking for some creativity. any questions, please ask. Attached an image that she liked for the image of the woman (would like to see versions of this included)
Updates

Target Market(s)

women 20+ that are new home owners or that are tackling Fixer Upper Diaries on their own

Industry/Entity Type

Fixer Upper Diaries

Requirements
Must have
• color coordinate with the website
should feature a young, blond, female caricature
should include the name of the website

```html
<!DOCTYPE html>
<html lang="en">
<head>
<meta charset="utf-8">
<title>Fixer Upper Diaries – Completed Projects</title>
<link rel="stylesheet" href="https://fonts.googleapis.com/css2?family=Roboto+Condensed:ital,wght@0,400;0,700;1,400;1,700&display=swap">
<style>
  :root {
    --room-light: #f1ece6;
    --room-warm: #d9c8b2;
    --shell-pink: #f7d4e4;
    --header-pink: #f5cfe0;
    --nav-maroon: #6e1446;
    --nav-active: #d8317c;
    --accent-pink: #e0287a;
    --deep-berry: #7d1e4e;
    --side-cream: #f3e7cf;
    --panel-pink: #fbe3ee;
    --text-dark: #2a1420;
    --free-red: #b0102a;
    --white: #ffffff;
    --video-black: #000000;
    --status-grey: #e9e9e9;
  }
  * { box-sizing: border-box; margin: 0; padding: 0; }
  html, body { width: 1200px; height: 900px; overflow: hidden; }
  body { position: relative; font-family: "Roboto Condensed", sans-serif; color: var(--text-dark); }

  .room-backdrop {
    position: absolute; inset: 0;
    background: linear-gradient(90deg, var(--room-light) 0%, #e8e2da 40%, #ece4d8 70%, var(--room-warm) 100%);
  }

  .page-shell {
    position: absolute; left: 143px; top: 50px; width: 901px; height: 860px;
    background: var(--shell-pink); border-radius: 14px 14px 0 0; overflow: hidden;
  }

  .site-header {
    position: absolute; left: 0; top: 0; width: 901px; height: 142px;
    background: linear-gradient(180deg, #fbe4ee 0%, var(--header-pink) 100%);
  }
  .brand-name {
    position: absolute; left: 24px; top: 10px;
    font-size: 34px; font-weight: 700; color: var(--accent-pink); letter-spacing: 0.5px;
  }
  .header-art {
    position: absolute; left: 317px; top: 0; width: 330px; height: 142px;
    background: radial-gradient(circle at 50% 55%, #c98fd8 0%, #d85ea0 45%, var(--header-pink) 80%);
  }

  .main-nav {
    position: absolute; left: 0; top: 142px; width: 901px; height: 65px;
    background: var(--nav-maroon); border-radius: 0 0 8px 8px;
    display: flex; list-style: none;
  }
  .main-nav li {
    display: flex; align-items: center; padding: 0 21px;
    color: var(--white); font-weight: 700; font-size: 16.5px;
  }
  .main-nav li:first-child { padding-left: 43px; }
  .main-nav .is-active { background: var(--nav-active); }

  .video-card {
    position: absolute; left: 15px; top: 245px; width: 562px; height: 525px;
    background: var(--white); border-radius: 6px;
  }
  .video-screen {
    position: absolute; left: 12px; top: 16px; width: 538px; height: 492px;
    background: var(--video-black); border: 2px solid #3d5668; border-radius: 4px;
  }

  .teaser-card {
    position: absolute; top: 800px; height: 60px; background: #efe1d2; border-radius: 4px;
  }
  .teaser-one { left: 9px; width: 275px; }
  .teaser-two { left: 297px; width: 275px; }

  .signup-column {
    position: absolute; left: 597px; top: 243px; width: 285px; height: 620px;
    background: var(--side-cream); border-radius: 4px;
  }
  .signup-panel {
    position: absolute; left: 12px; top: 44px; width: 263px; height: 580px;
    background: var(--white); border-radius: 4px; overflow: hidden;
  }
  .panel-swirl { position: absolute; right: 0; top: 0; }
  .guide-label {
    position: absolute; left: 10px; top: 24px;
    font-size: 25px; font-weight: 700; color: var(--accent-pink);
  }
  .guide-title {
    position: absolute; left: 24px; top: 76px; width: 214px; height: 110px;
    background: linear-gradient(180deg, #8e2a5d 0%, var(--deep-berry) 100%);
    border-radius: 4px; box-shadow: 0 2px 4px rgba(0,0,0,0.3);
    text-align: center; padding-top: 16px;
    font-size: 18px; font-weight: 700; line-height: 27px; color: var(--white);
  }
  .guide-title .pink { color: var(--accent-pink); }
  .guide-bonus {
    position: absolute; left: 0; top: 190px; width: 248px; text-align: center;
    font-style: italic; font-weight: 700; font-size: 15px; line-height: 29px; color: var(--text-dark);
  }
  .guide-bonus .free { color: var(--free-red); font-size: 26px; font-style: normal; font-weight: 400; }
  .guide-product {
    position: absolute; left: 48px; top: 254px; width: 150px; height: 130px;
    background: linear-gradient(135deg, #c84d97 0%, #e7a3c9 60%, #f2d1e3 100%);
  }
  .signup-form { position: absolute; left: 28px; top: 400px; width: 200px; }
  .form-row { display: flex; align-items: center; height: 30px; margin-bottom: 19px; font-style: italic; font-size: 16px; }
  .form-row label { width: 48px; }
  .form-row input { width: 142px; height: 30px; border: 1px solid #aaa; background: var(--white); }
  .download-btn {
    position: absolute; left: 77px; top: 498px; width: 143px; height: 34px;
    background: linear-gradient(180deg, #ec4f96 0%, var(--accent-pink) 100%);
    border: none; border-radius: 5px; color: var(--white);
    font-family: "Roboto Condensed", sans-serif; font-size: 18px;
  }

  .status-bar {
    position: absolute; left: 0; top: 873px; width: 395px; height: 27px;
    background: var(--status-grey); border: 1px solid #b9b9b9;
    font-family: "Roboto Condensed", sans-serif; font-size: 14px; line-height: 25px; padding-left: 2px; color: #222;
  }
</style>
</head>
<body>
  <div class="room-backdrop" role="img" aria-label="Bright living room under renovation with windows and shelving"></div>

  <div class="page-shell">
    <header class="site-header">
      <div class="brand-name">Fixer Upper Diaries</div>
      <div class="header-art" role="img" aria-label="Cartoon of a young blonde woman in a purple top against pink sunburst rays"></div>
    </header>

    <ul class="main-nav">
      <li>About Us</li>
      <li>Products</li>
      <li class="is-active">Completed Projects</li>
      <li>Share Your Project</li>
      <li>Articles</li>
      <li>How to Resources</li>
    </ul>

    <section class="video-card">
      <div class="video-screen" role="img" aria-label="Embedded project video"></div>
    </section>

    <div class="teaser-card teaser-one" role="img" aria-label="Project photo teaser"></div>
    <div class="teaser-card teaser-two" role="img" aria-label="Power tool photo teaser"></div>

    <aside class="signup-column">
      <div class="signup-panel">
        <svg class="panel-swirl" width="110" height="580" aria-hidden="true">
          <path d="M110 0 C40 80 20 170 70 260 C110 330 60 420 40 580 L110 580 Z" fill="var(--panel-pink)"/>
        </svg>
        <div class="guide-label">A FREE GUIDE</div>
        <div class="guide-title">10 QUESTIONS <span class="pink">TO ASK<br>BEFORE HIRING A</span><br>CONTRACTOR</div>
        <div class="guide-bonus">Receive Bonus How-to Videos and<br>Instructions All <span class="free">FREE</span></div>
        <div class="guide-product" role="img" aria-label="Guide booklet with two bonus DVDs"></div>
        <form class="signup-form">
          <div class="form-row"><label>Name:</label><input type="text"></div>
          <div class="form-row"><label>Email:</label><input type="text"></div>
        </form>
        <button class="download-btn" type="button">Download Now</button>
      </div>
    </aside>
  </div>

  <div class="status-bar">www.fixerupperdiaries.net/completed-projects/</div>
</body>
</html>
```